Lumeno-Interior design firm
Hello all,
I will announce the winner in the next few hours...
I appreciate your AMAZING ideas and all the many revisions that each of you submited, they helped us to understand your creative proposals and at the end to select a winner.
THANK YOU!
Lumeno Design
Draft #317 and #318
We are looking at some winning designs already and we will send our efforts towards those. i appreciate your entry very much.
Thanks!
Draft #312
The font on the subject LUMENO Interior design firm needs to be changed. I dont like it. I like the font used on the HOME, PORTFOLIO, etc...main subjects if that helps!
Everything else looks amazing!
hi all,
I had an unexpected business to attend today and I was not able to complete the feedback to all of you. We decided to extend the time to provide the missing feedback...I will provide to all, just give me some time.
I have decided to extend the contest. This was a last minute descision.
I appreciate your entry but is not what I am looking for. I don't want to waste your time as well as I prefer to concentrate on the designs/designers that have invested some time with me already.
Thank you and I appreciate your understanding!
Thanks brightquill! I really appreciate your understanding!
Draft #273
Can you justified all the texts used on each page? That will be great for final review.
Drafts #270 and #272
the text needs to be justified and that will make it!
Draft #269
HOME
There is a small misspell at the bottom left...it reads Lemeno instead of Lumeno.
Ater that revision you are set!
@PH, Thanks for your comments...
Dear Brightquill,
I like your entry but i am sorry to say that there is nothing original about it. I feel respect for everyones work and even when I am not an expert I feel you are copying other entries. I can not give you credit for someone else's ideas and I would appreciate if you come up with the same concept but with something that is your very own creation.
With all my respect...
Draft #251
Looks good just to revise the "yellow" cubes to be softer...and also please use my pictures for each page so I can compare with everyone else.
Thank you so much!
Draft #250
I would prefer to container the ABOUT US description on within the limits of the cubes so if necessary lets remove the "yellow" cubes so we can move up the wording and fit it within...
Use the service wording as reference...it is contained and it does not go below the "cubes"
Draft #249
lets list the services on a horizontal way inside the "cubes" Makes sense? linear way showing the services and the main wording as is.
Draft #248
can we made the windows with tabs LIVING, DINING, BEDROOM ACCENTS and KIDS to be one of the "cubes" from your design?
maybe using the bottom five...?
then when you click on I would like to see a complete picture...hopefully you come up with an idea but if not we can look at it together after revision...
Thanks
Draft #247
My only change is the "yellow" buttons to be more with softer colors...soft grey/white...or any suggestions within my request.
Draft #234
Wording needs to be consistent...I prefer white please revise.
Draft #227
Revisions:
I dont like the phone image under phone, please remove
Please do not underline the website
I prefer just letter on the front:
P: for phone
W: for website
etc...
In your case I would prefer not to use my picture...lets just remove it and after all this it should be done!
Looking good!
Draft #223
I need you to add the wording that I sent for services as well...it is important!
Thanks! Everything else looks perfect!
Hello@PH
I`m just waiting for your Feedback on
#221(Home page), #222(Portfolio Page), #223(Services Page),#224(About Us Page), & #225(Contact Page)
Zora
FOR EVERYONE:
PLEASE submit your complete designs, I wont be extending the project and with the time left I wont be able to give feedback and revisions to detail to everyone.
I really appreciate your hard work on attention to my project.
You ALL are very talented!
Good luck!
Draft #208 you can move forward with the inner pages.
Draft #207
I need the text to be justified please. You can complete your design with all he pages, I like the layout as is.
Look forward to final entries.

```html
<!DOCTYPE html>
<html lang="en">
<head>
<meta charset="utf-8">
<title>Lumeno – Interior Design Firm</title>
<link rel="stylesheet" href="https://fonts.googleapis.com/css2?family=Arimo:wght@400;700&family=Cinzel:wght@400&display=swap">
<style>
  :root {
    --page-bg: #e9e9ea;
    --page-bg-edge: #dcdcde;
    --logo-bg: #ffffff;
    --logo-gold: #b39a5c;
    --logo-grey: #8a8a8a;
    --frame: #ffffff;
    --panel: rgba(62, 50, 40, 0.72);
    --panel-line: rgba(255, 255, 255, 0.85);
    --text-light: #ffffff;
    --text-soft: #e6ddd2;
    --footer-text: #6f6f72;
    --icon: #9a9a9e;
  }
  * { box-sizing: border-box; margin: 0; padding: 0; }
  html, body { width: 1200px; height: 718px; overflow: hidden; }
  body {
    position: relative;
    font-family: "Arimo", Arial, sans-serif;
    background: radial-gradient(ellipse at center, var(--page-bg) 55%, var(--page-bg-edge) 100%);
  }
  .brand {
    position: absolute; left: 706px; top: 0; width: 226px; height: 104px;
    background: var(--logo-bg);
    display: flex; flex-direction: column; align-items: center; justify-content: center; gap: 4px;
  }
  .brand-row { display: flex; align-items: center; gap: 10px; }
  .brand-mark { width: 34px; height: 34px; border-radius: 50%; background: var(--logo-gold); }
  .brand-name { font-family: "Cinzel", serif; font-size: 30px; color: var(--logo-gold); letter-spacing: 1px; }
  .brand-tag { font-size: 9px; color: var(--logo-grey); margin-left: 40px; }

  .hero {
    position: absolute; left: 134px; top: 104px; width: 932px; height: 528px;
    border: 4px solid var(--frame);
    background: linear-gradient(120deg, #c9a98e 0%, #dcc6b0 28%, #b8926f 50%, #8a5e3c 68%, #e2d8c8 82%, #9c8770 100%);
  }
  .panel {
    position: absolute; left: 574px; top: 0; width: 224px; height: 100%;
    background: var(--panel);
    padding: 30px 18px 0;
  }
  .nav { list-style: none; display: flex; flex-direction: column; align-items: center; gap: 13px; }
  .nav a {
    display: inline-block; color: var(--text-light); text-decoration: none;
    font-size: 11px; letter-spacing: 0.3px; padding: 2px 5px;
  }
  .nav .is-current a { border: 1px solid var(--panel-line); }
  .panel-title { margin-top: 78px; font-size: 14px; font-weight: 700; color: var(--text-light); }
  .panel-text { margin-top: 18px; font-size: 11.5px; line-height: 16px; color: var(--text-soft); text-align: justify; }
  .contact { margin-top: 12px; list-style: none; font-size: 11.5px; line-height: 16px; color: var(--text-soft); }
  .contact b { color: var(--text-light); }

  .footer-brand { position: absolute; left: 156px; top: 648px; display: flex; align-items: center; gap: 8px; }
  .footer-mark { width: 28px; height: 28px; border-radius: 50%; background: var(--footer-text); }
  .footer-name { font-family: "Cinzel", serif; font-size: 22px; color: var(--footer-text); }
  .footer-nav { position: absolute; right: 142px; top: 648px; display: flex; gap: 22px; list-style: none; }
  .footer-nav a { font-size: 11px; color: var(--footer-text); text-decoration: none; }
  .social { position: absolute; right: 146px; top: 676px; display: flex; gap: 6px; }
  .social span { width: 16px; height: 16px; background: var(--icon); }
</style>
</head>
<body>
  <header class="brand">
    <div class="brand-row">
      <span class="brand-mark"></span>
      <span class="brand-name">LUMENO</span>
    </div>
    <span class="brand-tag">Interior design firm</span>
  </header>

  <main class="hero" role="img" aria-label="Photograph of a warm living room with leather armchairs, a sofa and a floor lamp">
    <section class="panel">
      <ul class="nav">
        <li><a href="#">HOME</a></li>
        <li><a href="#">PORTFOLIO</a></li>
        <li><a href="#">ABOUT US</a></li>
        <li><a href="#">SERVICES</a></li>
        <li class="is-current"><a href="#">CONTACT US</a></li>
      </ul>
      <h1 class="panel-title">LUMENO-Interior Design Firm</h1>
      <p class="panel-text">We will be honored to assist you with your projects or design ideas. Please contact us for further information.</p>
      <ul class="contact">
        <li><b>P:</b> 555.014.2260</li>
        <li><b>E:</b> you know I can not list it here...</li>
        <li><b>W:</b> lumeno-design.com</li>
      </ul>
    </section>
  </main>

  <footer>
    <div class="footer-brand">
      <span class="footer-mark"></span>
      <span class="footer-name">LUMENO</span>
    </div>
    <ul class="footer-nav">
      <li><a href="#">Home</a></li>
      <li><a href="#">Portfolio</a></li>
      <li><a href="#">About us</a></li>
      <li><a href="#">Services</a></li>
      <li><a href="#">Contact us</a></li>
    </ul>
    <div class="social" aria-label="Social links">
      <span></span><span></span>
    </div>
  </footer>
</body>
</html>
```